Business card logo

Hello, I would like a business card for my law firm with a logo composed of my initials "CV". The logo is intended to appear on my business card, my letterhead, envelope and documents from my office. My first and last name (Camille Vautrin) and "Lawyer" must appear next to the logo. I would like the logo and the characters to be in golden color on a dark background (example black, navy blue). I would especially like a refined work on the logo which should be composed of the letters J and R.

```html
<!DOCTYPE html>
<html lang="en">
<head>
<meta charset="utf-8">
<title>Camille Vautrin — Lawyer — Business Card</title>
<link rel="stylesheet" href="https://fonts.googleapis.com/css2?family=Cinzel:wght@500;600&family=Arimo:wght@400&display=swap">
<style>
  :root {
    --stage: #1c1c1e;
    --card: #1f1f21;
    --card-edge: #2a2a2d;
    --gold: #f2b21f;
    --gold-soft: #e8a915;
    --ink-light: #d9d9d9;
    --ink-white: #ffffff;
    --rule: #4a4a4d;
  }
  * { margin: 0; padding: 0; box-sizing: border-box; }
  html, body {
    width: 1200px; height: 900px; overflow: hidden;
    background: var(--stage);
  }
  .stage { position: relative; width: 1200px; height: 900px; }

  .card {
    position: absolute;
    width: 560px; height: 320px;
    background: var(--card);
    border: 1px solid var(--card-edge);
    box-shadow: 0 18px 40px rgba(0,0,0,.55);
  }
  .card--front { left: 380px; top: 90px; }
  .card--back  { left: 260px; top: 480px; }

  /* wordmark */
  .wordmark { display: flex; flex-direction: column; align-items: center; }
  .wordmark__name {
    font-family: "Cinzel", serif; font-weight: 600;
    color: var(--gold); font-size: 34px; letter-spacing: 1px; line-height: 1;
  }
  .wordmark__role {
    display: flex; align-items: center; gap: 10px; margin-top: 8px;
    font-family: "Cinzel", serif; font-weight: 500;
    color: var(--gold); font-size: 10px; letter-spacing: 8px;
  }
  .wordmark__role::before, .wordmark__role::after {
    content: ""; width: 56px; height: 1px; background: var(--gold-soft);
  }
  .wordmark__seal {
    width: 60px; height: 60px; border: 2px solid var(--gold);
    border-radius: 50%; margin-bottom: 18px;
  }

  .card--front .wordmark { position: absolute; left: 0; right: 0; top: 70px; }
  .front__web {
    position: absolute; left: 0; right: 0; top: 240px; text-align: center;
    font-family: "Arimo", sans-serif; color: var(--ink-white); font-size: 14px;
  }

  .card--back .wordmark { position: absolute; left: 20px; width: 270px; top: 86px; }
  .card--back .wordmark__name { font-size: 28px; }
  .card--back .wordmark__role::before, .card--back .wordmark__role::after { width: 44px; }
  .back__divider {
    position: absolute; left: 300px; top: 40px; width: 1px; height: 240px;
    background: linear-gradient(var(--card), var(--rule), var(--card));
  }
  .contact { position: absolute; left: 325px; top: 62px; font-family: "Arimo", sans-serif; }
  .contact__name {
    font-family: "Cinzel", serif; font-weight: 600; color: var(--gold);
    font-size: 19px; letter-spacing: 1px;
  }
  .contact__title { color: var(--ink-light); font-size: 14px; margin-bottom: 8px; }
  .contact__list { list-style: none; }
  .contact__item {
    display: flex; align-items: center; gap: 9px;
    color: var(--ink-light); font-size: 14px; line-height: 20px;
  }
  .contact__item svg { width: 12px; height: 12px; fill: var(--gold); flex: none; }
  .contact__address { color: var(--ink-light); font-size: 14px; line-height: 19px; margin-top: 10px; }
</style>
</head>
<body>
<main class="stage">
  <section class="card card--front" aria-label="Card front">
    <div class="wordmark">
      <div class="wordmark__seal"></div>
      <div class="wordmark__name">Camille Vautrin</div>
      <div class="wordmark__role">LAWYER</div>
    </div>
    <p class="front__web">www.vautrinlaw.com</p>
  </section>

  <section class="card card--back" aria-label="Card back">
    <div class="wordmark">
      <div class="wordmark__seal"></div>
      <div class="wordmark__name">Camille Vautrin</div>
      <div class="wordmark__role">LAWYER</div>
    </div>
    <div class="back__divider"></div>
    <div class="contact">
      <div class="contact__name">ADRIEN MOREAU</div>
      <div class="contact__title">Managing Director</div>
      <ul class="contact__list">
        <li class="contact__item">
          <svg viewBox="0 0 12 12"><path d="M1 4c0-2 1-3 3-3h4c2 0 3 1 3 3H8.5V3h-5v1zM2 5h8l1 6H1z"/></svg>
          055-214 380 617
        </li>
        <li class="contact__item">
          <svg viewBox="0 0 12 12"><path d="M3 0h6v12H3zM4 1.5v7.5h4V1.5z"/></svg>
          055-214 380 618
        </li>
        <li class="contact__item">
          <svg viewBox="0 0 12 12"><path d="M0 2h12v8H0zM1 3l5 4 5-4z"/></svg>
          contact@vautrinlaw.com
        </li>
        <li class="contact__item">
          <svg viewBox="0 0 12 12"><circle cx="6" cy="6" r="6"/></svg>
          www.vautrinlaw.com
        </li>
      </ul>
      <p class="contact__address">18, Rue Lamarck Paris<br>France, 75018.</p>
    </div>
  </section>
</main>
</body>
</html>
```